Business Card New Design for Corvella

We would like a new look on our business card, using the same style, the same colors blue, gray and white with similar font that is represented on the new Sell Sheet. We recently re-designed our Sell Sheets - I've attached a sell sheet file for your reference. I've also attached our current business card and our logo. Keep the same information listed on each side of the card.

Contact Information for Business Card

Use details given on example provided

Font styles to use
Other font styles liked:
• Myriad Regular and Bold

Colors

Designer to choose colors to be used in the design.

Requirements
Must have
• Current Information that was provided on the current business card. Colors Must use Blue, Gray and White, the same colors as the sell sheet example.

```html
<!DOCTYPE html>
<html lang="en">
<head>
<meta charset="utf-8">
<title>Corvella Business Card</title>
<link href="https://fonts.googleapis.com/css2?family=Source+Sans+3:wght@400;600;700&display=swap" rel="stylesheet">
<style>
  :root {
    --blue: #0d63c2;
    --blue-deep: #0a4fa3;
    --blue-light: #1f9ae0;
    --gray: #55585d;
    --gray-mid: #6f7277;
    --white: #ffffff;
    --card-bg: #f3f4f5;
    --backdrop: #d9dadc;
  }
  * { margin: 0; padding: 0; box-sizing: border-box; }
  html, body { width: 1200px; height: 780px; overflow: hidden; }
  body {
    background: var(--backdrop);
    font-family: "Source Sans 3", "Myriad Pro", sans-serif;
    position: relative;
  }
  .card {
    position: absolute;
    width: 540px;
    height: 308px;
    background: linear-gradient(135deg, var(--white), var(--card-bg));
    box-shadow: 0 6px 18px rgba(0,0,0,0.18);
    overflow: hidden;
  }
  .card-front { left: 40px; top: 150px; }
  .card-back { left: 620px; top: 322px; }
  .card-shapes { position: absolute; inset: 0; }

  .brand-name {
    position: absolute;
    font-weight: 600;
    color: var(--gray);
    letter-spacing: 7px;
    text-transform: uppercase;
  }
  .card-front .brand-name { left: 30px; top: 44px; font-size: 42px; }
  .card-back .brand-name { left: 290px; top: 26px; font-size: 38px; }

  .holder { position: absolute; right: 22px; top: 14px; text-align: right; }
  .holder-name { color: var(--blue); font-weight: 700; font-size: 17px; }
  .holder-title { color: var(--gray-mid); font-size: 13px; line-height: 1; }

  .company {
    position: absolute; left: 24px; top: 184px;
    color: var(--white); font-weight: 700; font-size: 25px;
  }
  .address {
    position: absolute; left: 26px; top: 218px;
    color: var(--white); font-size: 13.5px; line-height: 18px;
    list-style: none;
  }
  .address li { display: flex; align-items: center; gap: 6px; }
  .address .plain { padding-left: 20px; }

  .phones {
    position: absolute; left: 346px; top: 92px;
    color: var(--white); font-size: 13.5px; line-height: 19px;
    list-style: none;
  }
  .phones li { display: flex; align-items: center; gap: 6px; }
  .phones .toll { font-weight: 600; margin-bottom: 2px; }

  .icon { width: 14px; height: 14px; flex: none; }

  .service-list {
    position: absolute; list-style: none;
    color: var(--gray-mid); font-size: 14px; line-height: 21px;
  }
  .service-list li { display: flex; align-items: center; gap: 8px; }
  .service-list li::before {
    content: ""; width: 7px; height: 7px; border-radius: 50%;
    background: var(--blue); flex: none;
  }
  .services-main { left: 28px; top: 28px; }
  .services-extra { left: 300px; top: 112px; }

  .web-address {
    position: absolute; right: 30px; bottom: 13px;
    color: var(--white); font-size: 15px; letter-spacing: 2px; font-weight: 600;
  }
</style>
</head>
<body>

<section class="card card-front">
  <svg class="card-shapes" width="540" height="308" viewBox="0 0 540 308">
    <defs>
      <radialGradient id="frontBlue" cx="0.55" cy="0.45" r="0.7">
        <stop offset="0" stop-color="#1f9ae0"/>
        <stop offset="1" stop-color="#0a4fa3"/>
      </radialGradient>
    </defs>
    <path d="M0 164 H318 Q330 164 330 152 V72 Q330 62 342 62 H540 V308 H0 Z" fill="url(#frontBlue)"/>
  </svg>

  <div class="brand-name">Corvella</div>

  <div class="holder">
    <div class="holder-name">Marcus Hale</div>
    <div class="holder-title">CEO</div>
  </div>

  <div class="company">Corvella Technical Services, Inc.</div>

  <ul class="address">
    <li class="plain">4170 Alder Creek Road</li>
    <li class="plain">Brookfield, IL 60513</li>
    <li>
      <svg class="icon" viewBox="0 0 14 14"><circle cx="7" cy="7" r="7" fill="#fff"/><circle cx="7" cy="7" r="4" fill="none" stroke="#0d63c2" stroke-width="1.2"/><path d="M3 7 H11 M7 3 V11" stroke="#0d63c2" stroke-width="1"/></svg>
      www.corvella-ts.com
    </li>
    <li>
      <svg class="icon" viewBox="0 0 14 14"><circle cx="7" cy="7" r="7" fill="#fff"/><rect x="3.5" y="4.5" width="7" height="5" fill="none" stroke="#0d63c2" stroke-width="1"/><path d="M3.5 4.5 L7 7.5 L10.5 4.5" fill="none" stroke="#0d63c2" stroke-width="1"/></svg>
      mhale@corvella-ts.com
    </li>
  </ul>

  <ul class="phones">
    <li class="toll">Toll Free (888) 555-0142 x318</li>
    <li>
      <svg class="icon" viewBox="0 0 14 14"><circle cx="7" cy="7" r="7" fill="#fff"/><path d="M4.5 4 L6 4 L6.6 5.8 L5.7 6.5 Q6.5 8 7.8 8.6 L8.5 7.7 L10.2 8.3 L10.2 9.8 Q7 10 4.4 6.8 Z" fill="#0d63c2"/></svg>
      (815) 555-0190
    </li>
    <li>
      <svg class="icon" viewBox="0 0 14 14"><circle cx="7" cy="7" r="7" fill="#fff"/><rect x="4" y="5.5" width="6" height="4" fill="#0d63c2"/><rect x="5" y="3.5" width="4" height="2" fill="none" stroke="#0d63c2" stroke-width="0.9"/></svg>
      (815) 555-0173
    </li>
    <li>
      <svg class="icon" viewBox="0 0 14 14"><circle cx="7" cy="7" r="7" fill="#fff"/><rect x="5" y="3.5" width="4" height="7" rx="0.8" fill="#0d63c2"/></svg>
      (815) 555-0128
    </li>
  </ul>
</section>

<section class="card card-back">
  <svg class="card-shapes" width="540" height="308" viewBox="0 0 540 308">
    <path d="M150 252 L168 238 H540 V308 H150 Z" fill="#6c6f73"/>
    <path d="M162 262 L176 250 H540 V308 H162 Z" fill="#0d63c2"/>
  </svg>

  <div class="brand-name">Corvella</div>

  <ul class="service-list services-main">
    <li>Conveyors</li>
    <li>Target Sauce Applicators</li>
    <li>Target Topping Applicators</li>
    <li>Waterfall Topping Applicators</li>
    <li>Pepperoni/ Meat slicer / Applicators</li>
    <li>Portion Controlled filler Pumps</li>
  </ul>

  <ul class="service-list services-extra">
    <li>Dry Ingredient Applicators</li>
    <li>Check Weigh Conveyors</li>
    <li>Portion Compensators</li>
  </ul>

  <div class="web-address">WWW.CORVELLA-TS.COM</div>
</section>

</body>
</html>
```